Travel Group 'Lydgate Group' needs a new business card design

Lydgate Group is a diverse business specialising in bespoke, tailor made holidays to suit all budgets and we are specialists in planning exciting day/short trips to suit all markets. Our target market is very varied going from the corporate client and as well as people in the community who simply want to experience something special.
We are looking for a card design that will encourage people to look at our websites and social media platforms and to see for themselves the different facets to our business. It is essential that the card has social media icons for Facebook, Twitter and Instagram. We are looking for a card with a blank background with no pictures and for the front side to have the attached Lydgate logo. The card should have similar colour scheme to the attached Lydgate logo.
The card must have the following information on one side:
Maud Penrose
Business Development Manager
maudpenrose@lydgatevoyages.example
Lydgate Group, 87 Quarry Lane
Kilwinning, Ayrshire, Scotland KA19 4TN
+44 (0)1294 730182
And then the card must have the following on the second side:
(Lydgate logo)
(social media icons)
www.lydgatevoyages.example
www.lydgateoutings.example
Target Market(s)
Our target market is very varied going from the corporate client and as well as people in the community who simply want to experience something special.
Industry/Entity Type
Business
Contact Information for Business Card
Maud Penrose
+44 (0)1294 730182
(Lydgate logo)
(social media icons)
www.lydgatevoyages.example
www.lydgateoutings.example
Requirements
Must have
- It is essential that the card has social media icons for Facebook, Twitter & Instagram.
Should not have
- Should not have any images other than Lydgate logo.

```html
<!DOCTYPE html>
<html lang="en">
<head>
<meta charset="utf-8">
<title>Lydgate Group – Business Card</title>
<link href="https://fonts.googleapis.com/css2?family=Roboto:wght@400;500;700&display=swap" rel="stylesheet">
<style>
  :root {
    --bg: #2b2b2e;
    --purple: #5e3a98;
    --magenta: #d93a8c;
    --navy: #2c1f5e;
    --paper: #f1f1f2;
    --white: #ffffff;
    --accent-line: #d6509a;
  }
  * { box-sizing: border-box; margin: 0; padding: 0; }
  html, body { width: 1200px; height: 800px; overflow: hidden; }
  body {
    background: var(--bg);
    font-family: "Roboto", Arial, sans-serif;
    position: relative;
  }
  .card {
    position: absolute;
    top: 245px;
    width: 540px;
    height: 310px;
    border-radius: 18px;
    overflow: hidden;
  }
  .card--front {
    left: 40px;
    background: linear-gradient(120deg, var(--purple) 0%, #a23f94 50%, var(--magenta) 100%);
    color: var(--white);
  }
  .card--back {
    left: 620px;
    background: var(--paper);
  }

  /* Front */
  .holder { position: absolute; left: 32px; top: 34px; }
  .holder__name {
    font-weight: 700;
    font-size: 26px;
    letter-spacing: 1.5px;
    text-transform: uppercase;
    line-height: 1;
  }
  .holder__role { font-size: 15px; margin-top: 4px; }
  .holder__bar {
    width: 56px; height: 4px;
    background: var(--magenta);
    margin-top: 10px;
    border-radius: 2px;
  }
  .contacts {
    position: absolute;
    left: 250px;
    top: 158px;
    list-style: none;
    font-size: 14px;
    line-height: 1.3;
  }
  .contacts__item { display: flex; gap: 10px; margin-bottom: 9px; }
  .contacts__icon { width: 14px; height: 14px; flex: none; margin-top: 2px; fill: var(--white); }

  /* Back */
  .brand {
    position: absolute;
    left: 0; top: 0;
    width: 290px; height: 310px;
    display: flex; align-items: center; justify-content: center;
  }
  .brand__name {
    font-size: 38px;
    font-weight: 700;
    color: var(--navy);
    letter-spacing: 2px;
  }
  .divider {
    position: absolute;
    left: 290px; top: 62px;
    width: 1.5px; height: 190px;
    background: var(--accent-line);
  }
  .social {
    position: absolute;
    left: 400px; top: 118px;
    display: flex; gap: 12px;
    list-style: none;
  }
  .social__badge {
    width: 24px; height: 24px;
    border: 1.5px solid var(--magenta);
    border-radius: 50%;
  }
  .websites {
    position: absolute;
    left: 310px; right: 24px; top: 158px;
    text-align: right;
    color: var(--magenta);
    font-size: 14px;
    line-height: 1.35;
  }
</style>
</head>
<body>
  <section class="card card--front" aria-label="Business card front">
    <div class="holder">
      <h1 class="holder__name">Maud Penrose</h1>
      <p class="holder__role">Business Development Manager</p>
      <div class="holder__bar"></div>
    </div>
    <ul class="contacts">
      <li class="contacts__item">
        <svg class="contacts__icon" viewBox="0 0 24 24" aria-hidden="true"><path d="M6.6 10.8a15 15 0 0 0 6.6 6.6l2.2-2.2c.3-.3.7-.4 1-.2 1.1.4 2.3.6 3.6.6.6 0 1 .4 1 1V20c0 .6-.4 1-1 1C10.6 21 3 13.4 3 4c0-.6.4-1 1-1h3.5c.6 0 1 .4 1 1 0 1.3.2 2.5.6 3.6.1.3 0 .7-.2 1z"/></svg>
        <span>+44 (0)1294 730182</span>
      </li>
      <li class="contacts__item">
        <svg class="contacts__icon" viewBox="0 0 24 24" aria-hidden="true"><path d="M2 5h20v14H2z M2 5l10 8 10-8" fill="none" stroke="#fff" stroke-width="2"/><path d="M3 6l9 7 9-7v12H3z"/></svg>
        <span>maudpenrose@lydgatevoyages.example</span>
      </li>
      <li class="contacts__item">
        <svg class="contacts__icon" viewBox="0 0 24 24" aria-hidden="true"><path d="M12 2a7 7 0 0 0-7 7c0 5 7 13 7 13s7-8 7-13a7 7 0 0 0-7-7zm0 9.5A2.5 2.5 0 1 1 12 6.5a2.5 2.5 0 0 1 0 5z"/></svg>
        <span>Lydgate Group, 87 Quarry Lane<br>Kilwinning, Ayrshire, Scotland KA19 4TN</span>
      </li>
    </ul>
  </section>

  <section class="card card--back" aria-label="Business card back">
    <div class="brand">
      <span class="brand__name">LYDGATE</span>
    </div>
    <div class="divider"></div>
    <ul class="social" aria-label="Social media">
      <li class="social__badge"></li>
      <li class="social__badge"></li>
      <li class="social__badge"></li>
    </ul>
    <div class="websites">
      <p>www.lydgatevoyages.example</p>
      <p>www.lydgateoutings.example</p>
    </div>
  </section>
</body>
</html>
```